Business Card Needed for Tend A Patron card should be modern looking with black backgroun

We need a business card designed for a company called Tend A Patron. The business card should have a black background and use our exact logo which is attached. The contact information should be green font. We have additional logo files if needed. The business card should include our logo, our slogan and our contact information.

Target Market(s)

Sales Professionals

Industry/Entity Type

Business

Contact Information for Business Card

Use the information on our website www.tendapatron.example for contact information. The card should also have our slogan "Let us help you plant your referral seed.."

Requirements
Must have
• Black Background with Green Logo and Font

```html
<!DOCTYPE html>
<html lang="en">
<head>
<meta charset="utf-8">
<title>Tend A Patron – Business Card Options</title>
<link rel="stylesheet" href="https://fonts.googleapis.com/css2?family=Open+Sans:wght@300;400&display=swap">
<style>
  :root {
    --board: #e6e6e6;
    --frame: #ffffff;
    --frame-edge: #d2d2d2;
    --card-light: #2a2a2a;
    --card-dark: #131313;
    --band: #0b0b0b;
    --green: #17b04a;
    --green-text: #1fae4b;
    --grey-text: #8a8a8a;
    --wordmark: #8c8c8c;
    --label: #1a1a1a;
  }
  * { box-sizing: border-box; margin: 0; padding: 0; }
  html, body { width: 1200px; height: 1000px; overflow: hidden; }
  body {
    position: relative;
    background: var(--board);
    font-family: "Open Sans", Arial, sans-serif;
  }
  .option {
    position: absolute;
    background: var(--frame);
    border: 1px solid var(--frame-edge);
  }
  .option--front-1 { left: 8px; top: 58px; width: 579px; height: 421px; }
  .option--front-2 { left: 612px; top: 58px; width: 581px; height: 421px; }
  .option--back { left: 218px; top: 503px; width: 768px; height: 488px; }

  .card {
    position: absolute;
    overflow: hidden;
    background: radial-gradient(ellipse at 30% 25%, var(--card-light) 0%, var(--card-dark) 70%);
  }
  .option--front-1 .card,
  .option--front-2 .card { left: 10px; top: 8px; width: 558px; height: 318px; }
  .option--back .card {
    left: 23px; top: 19px; width: 716px; height: 410px;
    background: radial-gradient(ellipse at 45% 30%, #2c2c2c 0%, var(--card-dark) 75%);
  }

  .card__divider {
    position: absolute; left: 279px; top: 0; width: 1px; height: 278px;
    background: rgba(255,255,255,0.06);
  }
  .card__address {
    position: absolute; left: 324px; top: 67px;
    font-style: normal; font-weight: 300; font-size: 23px; line-height: 31px;
  }
  .card__band {
    position: absolute; left: 0; bottom: 0; width: 100%; height: 40px;
    background: var(--band);
    display: flex; align-items: center; justify-content: center;
    font-weight: 300; font-size: 22px;
  }
  .card__corner { position: absolute; bottom: 0; width: 58px; height: 48px; }
  .card__corner--left { left: 0; }
  .card__corner--right { right: 0; }

  .is-green { color: var(--green-text); }
  .is-grey { color: var(--grey-text); }

  .wordmark {
    position: absolute;
    display: flex; align-items: center; gap: 8px;
    color: var(--wordmark);
    font-weight: 400;
    white-space: nowrap;
  }
  .wordmark__dot { border-radius: 50%; background: var(--green); flex: none; }
  .wordmark--small { left: 54px; top: 143px; font-size: 20px; }
  .wordmark--small .wordmark__dot { width: 15px; height: 15px; }
  .wordmark--large { left: 50%; top: 59%; transform: translate(-50%, -50%); font-size: 44px; gap: 14px; }
  .wordmark--large .wordmark__dot { width: 30px; height: 30px; }

  .option__label {
    position: absolute; left: 0; width: 100%; text-align: center;
    color: var(--label); font-weight: 400; font-size: 36px;
  }
  .option--front-1 .option__label,
  .option--front-2 .option__label { top: 353px; }
  .option--back .option__label { top: 438px; }
</style>
</head>
<body>

<section class="option option--front-1">
  <div class="card">
    <div class="wordmark wordmark--small"><span class="wordmark__dot"></span>Tend A Patron</div>
    <div class="card__divider"></div>
    <address class="card__address is-green">
      Tend a Patron LLC<br>P.O.Box 218<br>Cedar Hollow,<br>MD 20614<br>USA
    </address>
    <div class="card__band is-green">morgan@tendapatron.example</div>
    <svg class="card__corner card__corner--left" viewBox="0 0 58 48"><polygon points="0,0 58,0 0,48" fill="var(--green)"/></svg>
    <svg class="card__corner card__corner--right" viewBox="0 0 58 48"><polygon points="0,0 58,0 58,48" fill="var(--green)"/></svg>
  </div>
  <p class="option__label">Front option - 1</p>
</section>

<section class="option option--front-2">
  <div class="card">
    <div class="wordmark wordmark--small"><span class="wordmark__dot"></span>Tend A Patron</div>
    <div class="card__divider"></div>
    <address class="card__address is-grey">
      Tend a Patron LLC<br>P.O.Box 218<br>Cedar Hollow,<br>MD 20614<br>USA
    </address>
    <div class="card__band is-grey">morgan@tendapatron.example</div>
    <svg class="card__corner card__corner--left" viewBox="0 0 58 48"><polygon points="0,0 58,0 0,48" fill="var(--green)"/></svg>
    <svg class="card__corner card__corner--right" viewBox="0 0 58 48"><polygon points="0,0 58,0 58,48" fill="var(--green)"/></svg>
  </div>
  <p class="option__label">Front option - 2</p>
</section>

<section class="option option--back">
  <div class="card">
    <div class="wordmark wordmark--large"><span class="wordmark__dot"></span>Tend A Patron</div>
  </div>
  <p class="option__label">Back</p>
</section>

</body>
</html>
```